Wordpress theme website for professionals working together

My partner and I are offering business services, my wife in the energy business as mainly as member of the board of commissioners. I am working as interim manager/consultant in the accounting and finance area. Both activities are connected in one company VELMORO BV (dutch ltd). We need a CV based website. Beside this we do some financial and accounting services.

Target Market(s)

small medium business

Font styles to use
Sans Serif

Colors

Designer to choose colors to be used in the design.

Requirements
Must have
• Pictures of both members.
• CLEAN AND SIMPLE
• I LIKE BLACK & WHITE
Nice to have
• I like design like this theme: http://theme.brindlepax.com/resume/

```html
<!DOCTYPE html>
<html lang="en">
<head>
<meta charset="utf-8">
<title>Velmoro BV</title>
<link rel="stylesheet" href="https://fonts.googleapis.com/css2?family=Poppins:wght@400;500;600;700&family=Open+Sans:wght@400;600&display=swap">
<style>
:root{
  --red:#e52521;
  --ink:#1d1d1d;
  --text:#555;
  --white:#fff;
  --line:#d9d9d9;
}
*{box-sizing:border-box;margin:0;padding:0}
html,body{width:747px;height:1200px;overflow:hidden;background:var(--white)}
body{font-family:"Open Sans",sans-serif;color:var(--text);position:relative}
.hero{position:absolute;left:0;top:0;width:747px;height:411px;overflow:hidden}
.hero-photo{position:absolute;inset:0;background:linear-gradient(160deg,#4a5566 0%,#6b5448 38%,#3b3430 65%,#2a2e33 100%)}
.hero-shade{position:absolute;inset:0;background:rgba(15,18,24,.45)}
.brand{position:absolute;left:95px;top:38px;font-family:"Poppins",sans-serif;font-weight:700;font-size:26px;color:var(--white);letter-spacing:.5px;display:flex;align-items:center;gap:8px}
.brand-mark{width:10px;height:10px;background:var(--red)}
.menu{position:absolute;right:60px;top:46px;width:20px}
.menu span{display:block;height:2px;background:var(--white);margin-bottom:4px}
.hero-title{position:absolute;left:0;right:0;top:172px;text-align:center;font-family:"Poppins",sans-serif;font-weight:700;font-size:40px;color:var(--white);letter-spacing:.5px}
.hero-text{position:absolute;left:190px;width:367px;top:238px;text-align:center;font-size:10px;line-height:15px;color:#e6e6e6}
.btn{display:inline-block;background:var(--red);color:var(--white);font-family:"Poppins",sans-serif;font-weight:500}
.hero-btn{position:absolute;left:331px;top:303px;width:86px;height:24px;line-height:24px;font-size:8px;text-align:center;text-transform:uppercase}
.about{position:absolute;left:0;top:411px;width:747px;height:596px}
.section-title{position:absolute;left:0;right:0;top:40px;text-align:center;font-family:"Poppins",sans-serif;font-weight:700;font-size:24px;color:var(--ink);letter-spacing:.5px}
.section-title em{font-style:normal;color:var(--red)}
.title-rule{position:absolute;left:328px;top:76px;width:90px;height:2px;background:var(--line)}
.title-rule::after{content:"";position:absolute;left:25px;top:0;width:40px;height:2px;background:var(--red)}
.about-text{position:absolute;left:140px;width:467px;top:104px;text-align:center;font-size:9.5px;line-height:16px;color:var(--text)}
.team{position:absolute;left:0;top:222px;width:747px}
.member{position:absolute;top:0;width:150px;text-align:center}
.member-first{left:143px}
.member-second{left:299px}
.member-third{left:455px}
.portrait{position:relative;width:140px;height:140px;margin:0 auto;border-radius:50%;overflow:hidden;background:radial-gradient(circle at 50% 40%,#c9c4bf 0%,#8f8984 55%,#5e5a57 100%)}
.portrait-name{position:absolute;left:0;right:0;bottom:0;height:52px;background:var(--red);color:var(--white);font-family:"Poppins",sans-serif;font-weight:600;font-size:11px;line-height:14px;padding-top:9px}
.member-role{margin-top:10px;font-family:"Poppins",sans-serif;font-weight:600;font-size:10.5px;color:var(--ink)}
.member-bio{margin:7px auto 0;width:140px;font-size:8px;line-height:12px;color:var(--text)}
.member-btn{margin-top:12px;width:56px;height:20px;line-height:20px;font-size:7px;text-align:center}
.slider-nav{position:absolute;top:540px;left:329px;display:flex;gap:14px}
.slider-nav span{width:30px;height:30px;border:1.5px solid var(--red);display:flex;align-items:center;justify-content:center}
.footer{position:absolute;left:0;top:1007px;width:747px;height:193px;overflow:hidden}
.footer-photo{position:absolute;inset:0;background:linear-gradient(150deg,#3a3530 0%,#2a2826 50%,#1e2125 100%)}
.footer-shade{position:absolute;inset:0;background:rgba(12,14,18,.6)}
.contact{position:absolute;top:30px;width:150px;text-align:center;color:var(--white)}
.contact-email{left:149px}
.contact-call{left:299px}
.contact-address{left:448px}
.contact-icon{width:40px;height:40px;margin:0 auto;border:1.5px solid var(--white);border-radius:50%;display:flex;align-items:center;justify-content:center}
.contact-label{margin-top:14px;font-family:"Poppins",sans-serif;font-weight:600;font-size:10px;letter-spacing:.5px}
.contact-value{margin-top:4px;font-size:9.5px;line-height:14px;color:#ddd}
.footer-bar{position:absolute;left:0;right:0;bottom:0;height:30px;border-top:1px solid rgba(255,255,255,.2);display:flex;align-items:center;justify-content:space-between;padding:0 62px 0 80px}
.social{display:flex;gap:9px}
.social span{width:8px;height:8px;border-radius:50%;background:var(--white)}
.copyright{font-size:8px;color:#ccc}
</style>
</head>
<body>
<header class="hero">
  <div class="hero-photo" role="img" aria-label="Photograph of a brick office building with tall windows"></div>
  <div class="hero-shade"></div>
  <div class="brand">VELMORO<span class="brand-mark"></span></div>
  <div class="menu"><span></span><span></span><span></span></div>
  <h1 class="hero-title">WELCOME TO VELMORO</h1>
  <p class="hero-text">We combine board experience in the energy sector with interim management in accounting and finance, offering small and medium businesses steady guidance, clear reporting and practical support whenever the work asks for it.</p>
  <a class="btn hero-btn">Learn More</a>
</header>

<main class="about">
  <h2 class="section-title">WHO <em>ARE WE</em></h2>
  <div class="title-rule"></div>
  <p class="about-text">Velmoro BV brings two professional paths together in one Dutch company. One partner serves on boards of commissioners in the energy business, guiding strategy and oversight. The other works as interim manager and consultant in accounting and finance, stepping in where teams need structure. Beside this we provide financial and accounting services for small and medium businesses, from bookkeeping and reporting to budgets and planning. We keep our work clear, personal and reliable, so clients always know where they stand and what comes next.</p>

  <div class="team">
    <div class="member member-first">
      <div class="portrait" role="img" aria-label="Portrait photo of Lena Voss">
        <div class="portrait-name">Lena<br>Voss</div>
      </div>
      <div class="member-role">Director Board</div>
      <p class="member-bio">Board member in the energy sector with long experience in governance, strategy and supervision of growing companies and their management teams.</p>
      <a class="btn member-btn">View Profile</a>
    </div>
    <div class="member member-second">
      <div class="portrait" role="img" aria-label="Portrait photo of Mark Delan">
        <div class="portrait-name">Mark<br>Delan</div>
      </div>
      <div class="member-role">Advisor Finance</div>
      <p class="member-bio">Interim manager and consultant in accounting and finance, helping businesses bring order to reporting, closing and control during periods of change.</p>
      <a class="btn member-btn">View Profile</a>
    </div>
    <div class="member member-third">
      <div class="portrait" role="img" aria-label="Portrait photo of Lena Voss">
        <div class="portrait-name">Lena<br>Voss</div>
      </div>
      <div class="member-role">Director Services</div>
      <p class="member-bio">Supports clients with financial and accounting services, from monthly bookkeeping and budgets to clear annual reports for small and medium firms.</p>
      <a class="btn member-btn">View Profile</a>
    </div>
  </div>

  <div class="slider-nav">
    <span><svg width="10" height="10" viewBox="0 0 10 10"><path d="M6.5 1.5 3 5l3.5 3.5" fill="none" stroke="#e52521" stroke-width="1.5"/></svg></span>
    <span><svg width="10" height="10" viewBox="0 0 10 10"><path d="M3.5 1.5 7 5 3.5 8.5" fill="none" stroke="#e52521" stroke-width="1.5"/></svg></span>
  </div>
</main>

<footer class="footer">
  <div class="footer-photo" role="img" aria-label="Dimmed photograph of a city street"></div>
  <div class="footer-shade"></div>
  <div class="contact contact-email">
    <div class="contact-icon"><svg width="18" height="14" viewBox="0 0 18 14"><rect x="1" y="1" width="16" height="12" fill="none" stroke="#fff" stroke-width="1.4"/><path d="M1 1l8 7 8-7" fill="none" stroke="#fff" stroke-width="1.4"/></svg></div>
    <div class="contact-label">EMAIL US</div>
    <div class="contact-value">info@velmoro-mail.com</div>
  </div>
  <div class="contact contact-call">
    <div class="contact-icon"><svg width="16" height="16" viewBox="0 0 16 16"><path d="M3 1.5l3 3-1.8 2a9 9 0 0 0 5.3 5.3l2-1.8 3 3-2 2C7 14.5 1.5 9 1 3.5z" fill="#fff"/></svg></div>
    <div class="contact-label">CALL US</div>
    <div class="contact-value">+31 (20) 555 0147</div>
  </div>
  <div class="contact contact-address">
    <div class="contact-icon"><svg width="14" height="18" viewBox="0 0 14 18"><path d="M7 1a6 6 0 0 0-6 6c0 4.5 6 10 6 10s6-5.5 6-10a6 6 0 0 0-6-6z" fill="#fff"/><circle cx="7" cy="7" r="2.3" fill="#2a2826"/></svg></div>
    <div class="contact-label">ADDRESS</div>
    <div class="contact-value">48 Linden Lane<br>Harbor City</div>
  </div>
  <div class="footer-bar">
    <div class="social"><span></span><span></span><span></span><span></span><span></span></div>
    <div class="copyright">Velmoro © All Rights Reserved</div>
  </div>
</footer>
</body>
</html>
```